Use your magic to make a startup company look established*

We are in need of a website that gives the appearance that we are established rather than new. Our audience is comprised of senior executives in technology professional services companies, financial people (conservative) that invest in them, and executives in companies that are in need of their services. The site therefore needs to lean towards the conservative side while being modern and professional.

This should be a fairly simple site.

- About us
- Services
- Contacts
- Content (Articles)

It should be SEO friendly and easy to add content or sub pages. A responsive design is mandatory.

Target Market(s)

We work with executives and investors in professional services companies to more effectively compete in the already crowded “digital transformation” market.

Industry/Entity Type

Professional Service

Coding

Coded - Design and coding required

Number of Pages Required

5+ page

Font styles to use
Sans Serif

Requirements
Must have
• - Responsive design
- Easy to add/change content
- Easy to add additional pages

```html
<!DOCTYPE html>
<html lang="en">
<head>
<meta charset="utf-8">
<title>Northgate Advisory</title>
<link href="https://fonts.googleapis.com/css2?family=Montserrat:wght@300;400;500;600;700;800&display=swap" rel="stylesheet">
<style>
:root{
  --gold:#b1832b;
  --gold-bright:#d4a531;
  --gold-line:#c9a24e;
  --navy:#2c313c;
  --ink:#1f1f1f;
  --muted:#6b6b6b;
  --soft:#efefef;
  --white:#ffffff;
}
*{margin:0;padding:0;box-sizing:border-box}
html,body{width:1200px;height:3393px;overflow:hidden}
body{font-family:'Montserrat',sans-serif;background:var(--white);color:var(--ink);position:relative}
.abs{position:absolute}

/* header */
.hero{position:absolute;left:0;top:0;width:1200px;height:658px;
  background:linear-gradient(180deg,#3b4150 0%,#4a505c 40%,#2d2b2c 75%,#1d1a19 100%)}
.nav{position:absolute;left:0;top:0;width:1200px;height:80px;border-bottom:1px solid rgba(255,255,255,.18)}
.nav a{position:absolute;top:31px;color:#e9e9e9;font-size:14px;text-decoration:none;letter-spacing:.3px}
.caret{display:inline-block;width:0;height:0;border-left:4px solid transparent;border-right:4px solid transparent;border-top:4px solid #e9e9e9;margin-left:6px;vertical-align:middle}
.brand{position:absolute;left:548px;top:18px;display:flex;align-items:center;gap:7px}
.brand-mark{width:18px;height:18px;background:var(--gold)}
.brand-name{color:#fff;font-size:13px;font-weight:600;letter-spacing:1.5px}
.skyline{position:absolute;left:0;top:80px;width:1200px;height:578px;
  background:linear-gradient(180deg,rgba(70,76,90,0) 0%,rgba(60,62,70,.4) 45%,rgba(120,85,45,.45) 78%,rgba(25,22,20,.9) 100%)}
.hero h1{position:absolute;left:0;top:200px;width:1200px;text-align:center;color:#fff;font-size:60px;font-weight:800;letter-spacing:2px}
.hero p{position:absolute;left:330px;top:288px;width:540px;text-align:center;color:#f0f0f0;font-size:11px;line-height:16px}
.btn-contact{position:absolute;left:514px;top:369px;width:171px;height:50px;background:var(--gold);color:#1d1d1d;font-size:12px;font-weight:600;display:flex;align-items:center;justify-content:center}

/* about */
.about{position:absolute;left:0;top:658px;width:1200px;height:550px;background:linear-gradient(90deg,#f1f1f1,#e9e9e9 60%,#ececec)}
.frame-gold{position:absolute;left:161px;top:56px;width:290px;height:305px;border:6px solid var(--gold-bright);border-right:none;border-bottom:none}
.frame-grey{position:absolute;left:450px;top:56px;width:120px;height:120px;border-top:6px solid #555;border-right:6px solid #555}
.frame-base{position:absolute;left:430px;top:300px;width:140px;height:165px;border-right:6px solid var(--gold);border-bottom:6px solid var(--gold)}
.photo-office{position:absolute;left:168px;top:63px;width:395px;height:394px;background:linear-gradient(160deg,#d9d8d4 0%,#b9b4aa 45%,#5a4c43 70%,#3a302c 100%)}
.about h2{position:absolute;left:634px;top:76px;font-size:23px;font-weight:400;letter-spacing:1px;color:var(--ink)}
.dashes{position:absolute;display:flex;gap:7px}
.dashes i{display:block;height:3px;background:var(--gold)}
.about .copy{position:absolute;left:634px;top:145px;width:390px;font-size:11.5px;line-height:17px;color:#333}
.about .copy p{margin-bottom:17px}
.about .rule{position:absolute;left:630px;top:340px;width:410px;height:1px;background:var(--gold-line)}
.feature{position:absolute;top:372px;width:110px;text-align:center}
.feature svg{display:block;margin:0 auto 14px}
.feature span{font-size:12px;font-weight:700;letter-spacing:.5px}

/* market */
.market{position:absolute;left:0;top:1208px;width:1200px;height:702px;background:var(--gold)}
.market h2{position:absolute;left:0;top:90px;width:1200px;text-align:center;color:#fff;font-size:22px;font-weight:700;letter-spacing:.5px}
.market .lede{position:absolute;left:0;top:134px;width:1200px;text-align:center;color:#f3e4c4;font-size:12.5px;line-height:21px}
.card{position:absolute;top:257px;width:257px;height:299px;background:#fff;border-radius:4px;text-align:center}
.card .badge{position:absolute;left:85px;top:34px;width:86px;height:86px;border-radius:50%;background:#e0ac2c;border:3px solid #6b5220;display:flex;align-items:center;justify-content:center}
.card h3{position:absolute;left:0;top:150px;width:257px;font-size:16px;font-weight:600;letter-spacing:1px}
.card p{position:absolute;left:22px;top:206px;width:213px;font-size:10px;line-height:15px;color:#555}

/* blog */
.blog{position:absolute;left:0;top:1910px;width:1200px;height:557px;background:var(--soft)}
.blog h2{position:absolute;left:0;top:48px;width:1200px;text-align:center;font-size:23px;font-weight:700;color:#333}
.post-hero{position:absolute;left:180px;top:138px;width:394px;height:240px;background:linear-gradient(120deg,#2a2d9a 0%,#4a2b9a 45%,#6e1a6d 100%)}
.meta{position:absolute;font-size:9.5px;color:#777;display:flex;align-items:center;gap:6px}
.meta .sep{width:1px;height:10px;background:#555}
.meta .note{width:8px;height:7px;background:var(--gold-bright)}
.post-title{position:absolute;font-size:12px;font-weight:700;letter-spacing:.5px;color:#222}
.post-title.lg{font-size:14.5px}
.post-text{position:absolute;font-size:9.5px;line-height:15px;color:#777}
.thumb{position:absolute;left:627px;width:128px;height:103px}

/* map */
.map{position:absolute;left:0;top:2467px;width:1200px;height:446px;background:linear-gradient(135deg,#eef1f5 0%,#e6ecef 50%,#dfe9e4 100%)}

/* footer */
.footer{position:absolute;left:0;top:2913px;width:1200px;height:340px;background:var(--gold);color:#fff}
.footer h4{position:absolute;top:57px;font-size:11px;font-weight:600;letter-spacing:.5px}
.footer .small{position:absolute;font-size:9.5px;line-height:12px;color:#fbeedd}
.f-brand{position:absolute;left:170px;top:56px;display:flex;align-items:center;gap:7px}
.f-brand .brand-mark{background:#fff}
.f-link{position:absolute;left:447px;display:flex;align-items:center;gap:10px;font-size:10px;color:#fbeedd}
.field{position:absolute;left:781px;width:196px;height:29px;background:#fff;border-radius:2px;font-size:8.5px;color:#999;padding-left:16px;line-height:29px;letter-spacing:.5px}
.submit{position:absolute;left:781px;top:245px;width:68px;height:29px;background:#fff;border-radius:2px;font-size:8.5px;color:#333;text-align:center;line-height:29px;font-weight:600}
.bottom-bar{position:absolute;left:0;top:3253px;width:1200px;height:49px;background:var(--gold);border-top:1px solid rgba(255,255,255,.25);text-align:center;font-size:8px;color:#fbeedd;line-height:49px;letter-spacing:.3px}
</style>
</head>
<body>

<section class="hero">
  <div class="skyline" role="img" aria-label="Night photograph of a downtown city skyline with lit skyscrapers"></div>
  <nav class="nav">
    <a style="left:198px">ABOUT<span class="caret"></span></a>
    <a style="left:311px">SERVICES<span class="caret"></span></a>
    <a style="left:444px">NEWS</a>
    <div class="brand"><span class="brand-mark"></span><span class="brand-name">NORTHGATE</span></div>
    <a style="left:745px">RESOURCES<span class="caret"></span></a>
    <a style="left:893px">CONTACT<span class="caret"></span></a>
    <a style="left:1025px">LOGIN</a>
  </nav>
  <h1>WELCOME TO NORTHGATE</h1>
  <p>Lorem ipsum dolor sit amet, consectetur adipiscing elit, sed do eiusmod tempor incididunt ut labore et dolore magna aliqua. Quis ipsum suspendisse ultrices gravida.</p>
  <div class="btn-contact">Contact Now</div>
</section>

<section class="about">
  <div class="frame-gold"></div>
  <div class="frame-grey"></div>
  <div class="frame-base"></div>
  <div class="photo-office" role="img" aria-label="Photograph of a bright office with desks, chairs and cabinets"></div>
  <h2>WELCOME TO NORTHGATE</h2>
  <div class="dashes" style="left:636px;top:113px"><i style="width:30px"></i><i style="width:14px"></i><i style="width:10px"></i></div>
  <div class="copy">
    <p>Lorem ipsum dolor sit amet, consectetur adipisicing elit, sed do eiusmod tempor incididunt ut labore et dolore magna aliqua.</p>
    <p>&nbsp;Ut enim ad minim veniam, quis nostrud exercitation ullamco laboris nisi ut aliquip ex ea commodo consequat.</p>
    <p>Sed ut perspiciatis unde omnis iste natus error sit voluptatem accusantium doloremque laudantium, totam rem aperiam, eaque ipsa quae ab illo inventore veritatis et quasi architecto beatae vitae dicta sunt explicabo.</p>
  </div>
  <div class="rule"></div>
  <div class="feature" style="left:622px">
    <svg width="54" height="48" viewBox="0 0 54 48" fill="none" stroke="#b1832b" stroke-width="2"><rect x="6" y="16" width="36" height="26" rx="3"/><circle cx="24" cy="29" r="8"/><circle cx="24" cy="29" r="3"/><path d="M42 22h8v14h-8M12 16V8h10v8"/></svg>
    <span>LOREM IPSUM</span>
  </div>
  <div class="feature" style="left:754px">
    <svg width="54" height="48" viewBox="0 0 54 48" fill="none" stroke="#b1832b" stroke-width="2"><rect x="6" y="4" width="12" height="38" rx="2"/><circle cx="32" cy="18" r="8"/><circle cx="32" cy="18" r="3"/><circle cx="42" cy="34" r="6"/><path d="M4 44h46"/></svg>
    <span>LOREM IPSUM</span>
  </div>
  <div class="feature" style="left:886px">
    <svg width="54" height="48" viewBox="0 0 54 48" fill="none" stroke="#b1832b" stroke-width="2"><circle cx="22" cy="16" r="10"/><circle cx="22" cy="16" r="4"/><circle cx="38" cy="24" r="6"/><rect x="6" y="32" width="42" height="12" rx="2"/></svg>
    <span>LOREM IPSUM</span>
  </div>
</section>

<section class="market">
  <h2>MARKET FOCUS</h2>
  <div class="lede">Our Goal is to provide you with custom manufacturing<br>solutions that will make you more competitive &amp; improve your profitability</div>
  <article class="card" style="left:175px">
    <div class="badge"><svg width="40" height="40" viewBox="0 0 40 40" fill="none" stroke="#2a2a2a" stroke-width="3"><circle cx="20" cy="16" r="10"/><circle cx="20" cy="16" r="4"/><path d="M13 24l-4 12 6-3 4 5M27 24l4 12-6-3-4 5"/></svg></div>
    <h3>LOREM IPSUM</h3>
    <p>Lorem ipsum dolor sit amet, consectetur adipiscing elit, sed do eiusmod tempor incididunt ut labore.</p>
  </article>
  <article class="card" style="left:471px">
    <div class="badge"><svg width="46" height="40" viewBox="0 0 46 40" fill="none" stroke="#2a2a2a" stroke-width="2.5"><circle cx="23" cy="9" r="5"/><path d="M15 22c0-5 4-8 8-8s8 3 8 8"/><circle cx="11" cy="26" r="4"/><circle cx="35" cy="26" r="4"/><path d="M3 38c0-4 4-7 8-7s8 3 8 7M27 38c0-4 4-7 8-7s8 3 8 7"/></svg></div>
    <h3>LOREM IPSUM</h3>
    <p>Lorem ipsum dolor sit amet, consectetur adipiscing elit, sed do eiusmod tempor incididunt ut labore.</p>
  </article>
  <article class="card" style="left:768px">
    <div class="badge"><svg width="44" height="40" viewBox="0 0 44 40" fill="none" stroke="#2a2a2a" stroke-width="2.5"><circle cx="28" cy="14" r="9" stroke-dasharray="4 2"/><circle cx="28" cy="14" r="3"/><circle cx="14" cy="28" r="8" stroke-dasharray="4 2"/><circle cx="14" cy="28" r="3"/></svg></div>
    <h3>LOREM IPSUM</h3>
    <p>Lorem ipsum dolor sit amet, consectetur adipiscing elit, sed do eiusmod tempor incididunt ut labore.</p>
  </article>
</section>

<section class="blog">
  <h2>BLOG</h2>
  <div class="dashes" style="left:561px;top:85px"><i style="width:33px"></i><i style="width:16px"></i><i style="width:10px"></i></div>

  <div class="post-hero" role="img" aria-label="Abstract blue and purple network illustration"></div>
  <div class="meta" style="left:180px;top:2317px;top:407px">December 2020 <span class="sep"></span><span class="note"></span> No Comments</div>
  <div class="post-title lg" style="left:181px;top:427px">LOREM IPSUM DOLOR SIT AMET</div>
  <div class="post-text" style="left:181px;top:456px;width:350px">Lorem ipsum dolor sit amet, consectetur adipiscing elit, sed do eiusmod tempor incididunt ut labore et dolore magna aliqua. Quis ipsum suspendisse ultrices gravida.</div>

  <div class="thumb" style="top:140px;background:linear-gradient(135deg,#1d2436,#2a3148 55%,#c88a5c)" role="img" aria-label="Abstract dark illustration with flowing white and orange shapes"></div>
  <div class="meta" style="left:790px;top:148px">December 2020 <span class="sep"></span><span class="note"></span> No Comments</div>
  <div class="post-title" style="left:790px;top:173px">LOREM IPSUM DOLOR SIT AMET</div>
  <div class="post-text" style="left:790px;top:195px;width:210px">Lorem ipsum dolor sit amet, consectetur adipiscing elit, sed do eiusmod tempor incididunt ut labore et dolore.</div>

  <div class="thumb" style="top:265px;background:radial-gradient(circle at 50% 40%,#2a7fc4,#13457a 80%)" role="img" aria-label="Textured deep blue abstract background"></div>
  <div class="meta" style="left:790px;top:273px">December 2020 <span class="sep"></span><span class="note"></span> No Comments</div>
  <div class="post-title" style="left:790px;top:298px">LOREM IPSUM DOLOR SIT AMET</div>
  <div class="post-text" style="left:790px;top:320px;width:210px">Lorem ipsum dolor sit amet, consectetur adipiscing elit, sed do eiusmod tempor incididunt ut labore et dolore.</div>

  <div class="thumb" style="top:400px;background:linear-gradient(100deg,#1a1446,#4b1a6b 40%,#c52a6a 55%,#1d1850 80%)" role="img" aria-label="Abstract dark illustration with glowing pink light streaks"></div>
  <div class="meta" style="left:790px;top:408px">December 2020 <span class="sep"></span><span class="note"></span> No Comments</div>
  <div class="post-title" style="left:790px;top:433px">LOREM IPSUM DOLOR SIT AMET</div>
  <div class="post-text" style="left:790px;top:455px;width:210px">Lorem ipsum dolor sit amet, consectetur adipiscing elit, sed do eiusmod tempor incididunt ut labore et dolore.</div>
</section>

<div class="map" role="img" aria-label="Street map showing the office location and surrounding businesses"></div>

<footer class="footer">
  <div class="f-brand"><span class="brand-mark"></span><span class="brand-name">NORTHGATE</span></div>
  <div class="small" style="left:170px;top:135px;width:215px">Lorem ipsum dolor sit amet, conse ctetur adipiscing elit, sed do eiusmod tempor incididunt ut labore et dolore magna aliqua.</div>
  <div class="small" style="left:170px;top:195px;width:215px">Quis ipsum suspendisse ultrices gra vida. Risus commodo viverra mae ce nas accumsan lacus vel facilisis.</div>

  <h4 style="left:444px">SOCIAL MEDIA</h4>
  <div class="dashes" style="left:446px;top:93px"><i style="width:28px;background:#fff"></i><i style="width:12px;background:#fff"></i><i style="width:8px;background:#fff"></i></div>
  <div class="f-link" style="top:130px"><svg width="10" height="10"><circle cx="5" cy="5" r="4" fill="#fff"/></svg>Social Feed</div>
  <div class="f-link" style="top:160px"><svg width="10" height="10"><circle cx="5" cy="5" r="4" fill="#fff"/></svg>Video Channel</div>
  <div class="f-link" style="top:189px"><svg width="10" height="10"><circle cx="5" cy="5" r="4" fill="#fff"/></svg>Photo Stream</div>

  <h4 style="left:598px">CONTACT</h4>
  <div class="dashes" style="left:600px;top:93px"><i style="width:28px;background:#fff"></i><i style="width:12px;background:#fff"></i><i style="width:8px;background:#fff"></i></div>
  <div class="f-link" style="left:591px;top:128px"><svg width="12" height="12" viewBox="0 0 12 12"><circle cx="6" cy="6" r="5.5" fill="#fff"/><path d="M6 3v3l2 1.5" stroke="#b1832b" stroke-width="1.2" fill="none"/></svg>9.00 PM - 9.00 AM</div>
  <div class="f-link" style="left:591px;top:155px;align-items:flex-start"><svg width="12" height="14" viewBox="0 0 12 14"><path d="M3 1h3l1 3-2 1.5a8 8 0 0 0 3 4L10 8l2 1v3l-2 1C5 12 1 7 1 3z" fill="#fff"/></svg><span>(555) 010-2040<br>(800) 555-0134 toll-free</span></div>

  <h4 style="left:780px">STAY IN TOUCH</h4>
  <div class="dashes" style="left:781px;top:93px"><i style="width:28px;background:#fff"></i><i style="width:12px;background:#fff"></i><i style="width:8px;background:#fff"></i></div>
  <div class="small" style="left:781px;top:128px;color:#e8cf9a">Subscribe to our newsletter:</div>
  <div class="field" style="top:149px">YOUR NAME</div>
  <div class="field" style="top:196px">YOUR EMAIL</div>
  <div class="submit">SUBMIT</div>
</footer>
<div class="bottom-bar">2020 MERIDIAN WORKS | ALL RIGHTS RESERVED</div>

</body>
</html>
```